Private London College Prospectus

A single spread to begin with followed by treatments for a couple of awkward spreads in the brochure. Attached docs include previous few years to show how the design has evolved. We're now looking for a different direction
Outline: Private college in Central London.
Mainly A-levels but also GCSE courses
Consistently at the top of London results table
Operated by the owners
Prospectus is sent to anyone enquiring about the college

Target Market(s)

High net worth families in the Uk and abroad

Industry/Entity Type

College

Requirements
Must have
• Modern fonts
• House colour is purple - PMS 8804
• Teacher quote
• Page quote
Nice to have
• See attachments - the gryphon is part of their logo but not essential
Should not have
• Shouldn't be too fussy or cluttered
• No script fonts (probably) no italics in main text

```html
<!DOCTYPE html>
<html lang="en">
<head>
<meta charset="utf-8">
<title>The Harcourt Ethos – Prospectus Spread</title>
<link href="https://fonts.googleapis.com/css2?family=Montserrat:wght@400;500;600;700&family=Open+Sans:wght@400;600;700&display=swap" rel="stylesheet">
<style>
  :root {
    --purple: #5e3a87;
    --purple-dark: #472b68;
    --purple-tint: #efe9f5;
    --ink: #24212a;
    --paper: #fcfbfd;
    --backdrop: #e6e6e6;
    --frame: #d3cdd9;
    --white: #ffffff;
  }
  * { box-sizing: border-box; margin: 0; padding: 0; }
  html, body { width: 1200px; height: 900px; overflow: hidden; }
  body {
    background: var(--backdrop);
    font-family: "Open Sans", Arial, sans-serif;
    color: var(--ink);
    position: relative;
  }
  .spread {
    position: absolute; left: 60px; top: 68px;
    width: 1080px; height: 763px;
    display: flex;
    box-shadow: 0 10px 30px rgba(0,0,0,0.18);
  }
  .page {
    position: relative; width: 540px; height: 763px;
    background: var(--paper); overflow: hidden;
  }
  .page--left { border-right: 1px solid #ddd8e2; }
  .page-foot {
    position: absolute; left: 0; right: 0; bottom: 0; height: 12px;
    background: var(--purple);
  }

  /* Left page */
  .brand {
    position: absolute; top: 36px; left: 36px;
    display: flex; align-items: center; gap: 8px;
    font-family: "Montserrat", Arial, sans-serif;
    font-size: 17px; font-weight: 600; color: var(--purple);
  }
  .brand-dot { width: 14px; height: 14px; border-radius: 50%; background: var(--purple); }
  .tagline-band {
    position: absolute; top: 34px; left: 170px; right: 0; height: 26px;
    background: var(--purple); color: var(--white);
    font-family: "Montserrat", Arial, sans-serif;
    font-size: 10.5px; font-weight: 600; letter-spacing: 0.1em;
    display: flex; align-items: center; justify-content: center;
    text-transform: uppercase;
  }
  .page-title {
    position: absolute; top: 76px; left: 130px; right: 24px;
    font-family: "Montserrat", Arial, sans-serif;
    font-size: 34px; font-weight: 500; color: var(--ink);
    padding-bottom: 8px; border-bottom: 1px solid #b3a8bf;
  }
  .intro-band {
    position: absolute; top: 140px; left: 130px; right: 24px;
    background: var(--purple); color: var(--white);
    font-size: 10.5px; line-height: 1.45; padding: 10px 14px;
  }
  .why {
    position: absolute; top: 238px; left: 32px; width: 200px;
  }
  .why-heading {
    display: flex; align-items: flex-end; gap: 6px; margin-bottom: 8px;
    font-family: "Montserrat", Arial, sans-serif; color: var(--purple);
  }
  .why-heading .big { font-size: 26px; font-weight: 700; line-height: 1; }
  .why-heading .small { font-size: 9.5px; font-weight: 700; line-height: 1.15; color: var(--ink); }
  .body-copy {
    font-size: 10.5px; line-height: 1.36; text-align: justify;
  }
  .body-copy p + p { margin-top: 8px; }
  .photo {
    position: absolute; border: 5px solid var(--white);
    outline: 1px solid var(--frame);
  }
  .photo--classroom {
    top: 242px; left: 250px; width: 262px; height: 160px;
    background: linear-gradient(135deg, #c7b9a4, #8e8a84 55%, #5f6670);
  }
  .photo--study {
    top: 418px; left: 250px; width: 262px; height: 156px;
    background: linear-gradient(135deg, #d9d6cf, #9b8f82 50%, #6c6a68);
  }
  .page-quote {
    position: absolute; top: 652px; left: 32px; right: 28px;
    border-left: 4px solid var(--purple);
    background: var(--purple-tint);
    padding: 12px 16px;
  }
  .page-quote p {
    font-family: "Montserrat", Arial, sans-serif;
    font-size: 14px; font-weight: 500; line-height: 1.4; color: var(--purple-dark);
  }

  /* Right page */
  .photo--group {
    position: absolute; top: 26px; left: 30px; right: 30px; height: 300px;
    border: 6px solid var(--purple);
    background: linear-gradient(160deg, #3a3f3a, #23282c 45%, #8a8f80 80%, #c9c09a);
  }
  .section-band {
    position: absolute; top: 336px; left: 30px; right: 30px; height: 26px;
    background: var(--purple); color: var(--white);
    font-family: "Montserrat", Arial, sans-serif;
    font-size: 10.5px; font-weight: 600; letter-spacing: 0.06em;
    display: flex; align-items: center; justify-content: center;
    text-transform: uppercase;
  }
  .students {
    position: absolute; top: 374px; left: 40px; right: 40px;
  }
  .quote-box {
    position: absolute; top: 566px; left: 60px; right: 30px; height: 160px;
    border: 6px solid var(--purple); background: var(--white);
  }
  .quote-tab {
    position: absolute; top: -14px; right: 14px;
    background: var(--purple); color: var(--white);
    font-family: "Montserrat", Arial, sans-serif;
    font-size: 10px; font-weight: 600; letter-spacing: 0.08em;
    padding: 5px 10px; text-transform: uppercase;
  }
  .photo--teacher {
    position: absolute; top: 16px; left: 14px; width: 140px; height: 104px;
    border: 4px solid var(--frame);
    background: linear-gradient(135deg, #f1f1f1, #c8c8c6 60%, #8f8c88);
  }
  .quote-text {
    position: absolute; top: 26px; left: 172px; right: 18px;
  }
  .teacher-name { font-family: "Montserrat", Arial, sans-serif; font-size: 10.5px; font-weight: 700; text-transform: uppercase; }
  .teacher-role { font-size: 10.5px; font-weight: 700; color: var(--purple); margin-bottom: 6px; }
  .teacher-quote { font-size: 11.5px; line-height: 1.35; }
</style>
</head>
<body>
<main class="spread">
  <section class="page page--left">
    <div class="brand"><span class="brand-dot"></span>Harcourt</div>
    <div class="tagline-band">A modern college with a traditional approach</div>
    <h1 class="page-title">The Harcourt Ethos</h1>
    <p class="intro-band">Based in the heart of Kingsbridge in central London, Harcourt is a top performing independent sixth-form college, offering a broad A-level and GCSE curriculum for students from public, state and private school backgrounds.</p>

    <article class="why">
      <div class="why-heading"><span class="big">WHY</span><span class="small">Choose<br>Harcourt?</span></div>
      <div class="body-copy">
        <p>The majority of students who come to Harcourt do so because of our reputation for excellent A-level and GCSE results. This is true of students both on our full two-year programme as well as those on the one-year intensive programme. Most students will progress on to a top 20 UK university.</p>
        <p>Students are taught very much by traditional methods, in small groups, concentrating on the skills needed to pass examinations and to be successful at university. All teachers at Harcourt are subject specialists and most have experience as examiners. They are particularly successful with young people; they are able to motivate and communicate with them in ways which they understand. Barriers are quickly broken down, enhancing the learning process.</p>
      </div>
    </article>

    <div class="photo photo--classroom" role="img" aria-label="Photo of a small class seated around desks in a bright classroom"></div>
    <div class="photo photo--study" role="img" aria-label="Photo of two students working together at a desk"></div>

    <blockquote class="page-quote">
      <p>“Small groups, specialist teachers and a real partnership with parents – that is what sets Harcourt apart.”</p>
    </blockquote>
    <div class="page-foot"></div>
  </section>

  <section class="page page--right">
    <div class="photo--group" role="img" aria-label="Photo of a group of five students standing outside the college entrance"></div>
    <h2 class="section-band">How do we get the best out of our students?</h2>
    <div class="students body-copy">
      <p>Students benefit from individually tailored attention outside of classes – a key element of our successful A-level and GCSE programmes, and at Harcourt each student has a Curriculum Manager and a Personal Tutor, who provide advice on study skills, subject choices and careers, and who also monitor progress in regular meetings with students.</p>
      <p>We expect full commitment from our students and as such we have strict rules on attendance and timely submission of assignments. Parents are able to monitor progress through monthly reports, easily accessible using our online reporting system. Parents' Evenings are held during the Autumn and Spring terms.</p>
      <p>We encourage our students every step of the way and we help them to build confidence through examination success. We see the learning process as a successful partnership between students, tutors and parents.</p>
    </div>

    <aside class="quote-box">
      <span class="quote-tab">Teacher quote</span>
      <div class="photo--teacher" role="img" aria-label="Portrait photo of the Head of Economics"></div>
      <div class="quote-text">
        <p class="teacher-name">Rohan Mehta</p>
        <p class="teacher-role">Head of Economics</p>
        <p class="teacher-quote">We teach students how to develop their powers of analysis and independence of thought – crucial to success at university and beyond.</p>
      </div>
    </aside>
    <div class="page-foot"></div>
  </section>
</main>
</body>
</html>
```